Clean, Corporate redesign of existing website

We require a clean corporate professional redesign of our existing poor website, although a simple and elegant structure is required we would like the designer to concentrate on the little things and finishes to give the site a highly professional feel.
The company have supplied the following websites as to use as inspiration http://www.tollardminerals.com/ they like the clean, professional feel of the website
and the fact that the website captures the feel of their industry. Another clean and professional site they liked the look of was http://www.brindlefishbites.co.uk/ .
Another inspirational (page level only) http://www.harrowgateexpohall.com/thefacilities/floor-maps-and-specifications/ we like the top image and the corporate feel the images give. Auto cad drawings as images or a search for electrical services will fetch up a good selection of images to use as placeholders
A full brief, logos, images etc have been supplied
update: the sector is industrial electrical services, so more towards factory switches and equipement, not domestic light-bulbs etc this is important when choosing images for the site.
Updates
Thank you all for your designs, i will be presenting the best to the company tomorrow who will pick the design that suits so please get any remaining designs to me by tomorrow morning (GMT time) at the latest to be included in the presentation.
Target Market(s)
Business owners and CEO'S
Industry/Entity Type
Electrical
Look and feel

```html
<!DOCTYPE html>
<html lang="en">
<head>
<meta charset="utf-8">
<title>Fenwold Electrical Services Limited</title>
<link rel="stylesheet" href="https://fonts.googleapis.com/css2?family=Open+Sans:ital,wght@0,400;0,600;0,700;1,800&family=Ubuntu:wght@400;500&display=swap">
<style>
:root{
  --orange:#f26531;
  --orange-dark:#d9531e;
  --orange-line:#f58a60;
  --ink:#1e1e1e;
  --ink-soft:#3a3a3a;
  --grey:#8a8a8a;
  --paper:#f7f6f2;
  --panel-edge:#c9c9c9;
  --white:#ffffff;
  --navy:#3c2a7a;
  --red:#c4161c;
}
*{margin:0;padding:0;box-sizing:border-box}
html,body{width:1130px;height:1200px;overflow:hidden}
body{position:relative;background:var(--paper);font-family:"Open Sans",Verdana,sans-serif;color:var(--ink)}
.abs{position:absolute}

.masthead{left:0;top:0;width:1130px;height:128px;background:radial-gradient(ellipse 520px 120px at 565px 40px,#ffffff 0%,#ececec 70%,#d9d9d9 100%)}
.brand{left:120px;top:26px;display:flex;align-items:center;gap:12px}
.brand-mark{width:26px;height:26px;background:var(--orange);flex:none}
.brand-name{font-family:"Open Sans",sans-serif;font-size:24px;font-weight:600;line-height:29px;color:var(--ink-soft)}
.badge{top:25px;height:44px;border-radius:22px}
.badge-one{left:848px;width:82px;background:var(--navy)}
.badge-two{left:942px;top:30px;width:86px;height:30px;border-radius:3px;background:var(--red)}

.slider{left:99px;top:128px;width:933px;height:243px;border:2px solid var(--white);overflow:hidden}
.slider-photo{position:absolute;inset:0;background:linear-gradient(100deg,#2d4a7a 0%,#7a8aa8 28%,#c8b48c 45%,#6f7f96 65%,#c9ccd1 85%,#a58b72 100%)}
.slider-caption{position:absolute;font-family:"Open Sans",sans-serif;font-style:italic;font-weight:800;color:var(--orange);-webkit-text-stroke:1px var(--white);letter-spacing:1px;white-space:nowrap;font-size:30px}
.cap-one{top:162px;left:196px}
.cap-two{top:203px;right:16px}
.slider-pager{position:absolute;top:10px;right:20px;display:flex;gap:6px}
.slider-pager span{width:13px;height:13px;background:#333;color:var(--white);font-size:9px;line-height:13px;text-align:center}
.slider-pager span.on{background:var(--white);color:#333}
.slider-arrow{position:absolute;top:94px}

.main-nav{left:0;top:371px;width:1130px;height:53px;background:var(--orange)}
.main-nav ul{list-style:none;display:flex;margin-left:100px;height:100%}
.main-nav li{color:var(--white);font-family:Arial,Helvetica,sans-serif;font-size:14px;line-height:53px;padding:0 19px;border-right:1px solid var(--orange-dark);box-shadow:1px 0 0 var(--orange-line)}
.main-nav li:last-child{border:none;box-shadow:none}

.intro{left:117px;top:452px;width:632px}
.intro h1{font-family:"Open Sans",sans-serif;font-size:25px;font-weight:700;color:var(--orange);letter-spacing:.4px;margin-bottom:4px}
.intro p{font-size:12px;line-height:15.8px;text-align:justify;margin-bottom:15.8px;letter-spacing:.55px}

.clients{left:118px;top:792px;width:630px;height:86px;border:1px solid #c8c8c8;border-radius:8px;background:var(--white);display:flex;align-items:center;justify-content:space-around;padding:0 10px}
.client{font-size:13px;font-weight:700;color:#555;display:flex;align-items:center;gap:6px;text-align:center;line-height:1.2}
.client i{display:block;width:12px;height:12px;background:var(--orange);flex:none}
.clients-tail{left:368px;top:876px}
.clients-label{left:180px;top:890px;font-family:"Ubuntu",sans-serif;font-size:20px;color:var(--orange)}

.sidebar{left:766px;top:454px;width:248px;height:455px;border:1px solid var(--panel-edge);border-radius:6px;background:linear-gradient(#f3f3f3,#e9e9e9)}
.sidebar h2{font-family:"Ubuntu",sans-serif;font-weight:400;font-size:21px;color:var(--orange);text-align:center;margin-top:10px}
.sidebar-photo{margin:6px 0 0 15px;width:220px;height:101px;border:1px solid #333;background:linear-gradient(90deg,#b9bcc0,#e4e5e6 40%,#8e9196 70%,#cfd1d4)}
.sidebar-text{margin:8px 0 0 16px;width:220px;font-size:12px;line-height:13px;letter-spacing:.3px}
.service-list{list-style:none;margin:10px 0 0 26px;font-size:12px;font-weight:600;line-height:14px;letter-spacing:.5px}
.service-list li::before{content:"\2192";font-weight:400;margin-right:5px;color:#444}
.more{text-align:right;margin:24px 16px 0 0;font-size:9px;color:var(--red)}
.more::after{content:" \25B8"}
.sidebar hr{border:none;border-top:1px dashed #b8b8b8;margin:14px 20px 0}
.social-title{text-align:left!important;margin-left:22px}
.social{display:flex;gap:16px;margin:12px 0 0 22px}
.social span{width:58px;height:58px;border-radius:9px;background:#2f7fb8;color:var(--white);font-size:10px;font-weight:600;display:flex;align-items:center;justify-content:center}

.footer{left:0;top:923px;width:1130px;height:246px;background:var(--orange);color:var(--white)}
.footer h3{position:absolute;top:34px;font-family:"Ubuntu",sans-serif;font-weight:400;font-size:21px;color:#fde0d2}
.footer-links{position:absolute;left:118px;top:74px;list-style:none;font-size:14px;font-weight:600;line-height:26px;color:#fde8de}
.footer-rule{position:absolute;top:62px;width:1px;height:122px;background:#f7a07e}
.quote{position:absolute;left:416px;top:78px;width:258px;font-size:12.5px;line-height:15px;letter-spacing:.3px;color:#fde8de}
.quote-by{position:absolute;left:416px;top:194px;font-size:15px;font-weight:700;letter-spacing:.5px}
.contact{position:absolute;left:836px;top:76px;font-size:12.5px;line-height:15px;letter-spacing:.6px;color:#fde8de}
.contact .tel{margin-top:15px}
.contact .tel b{font-weight:400;margin-right:22px}
.base{left:0;top:1169px;width:1130px;height:31px;background:var(--orange-dark);border-top:1px solid #f59b77;color:#fde0d2;font-size:9.5px;text-align:center;line-height:30px}
</style>
</head>
<body>

<header class="masthead abs">
  <div class="brand abs">
    <span class="brand-mark"></span>
    <div class="brand-name">Fenwold Electrical<br>Services Limited</div>
  </div>
  <div class="badge badge-one abs" aria-label="Accreditation badge"></div>
  <div class="badge badge-two abs" aria-label="Registration badge"></div>
</header>

<section class="slider abs">
  <div class="slider-photo" role="img" aria-label="Electrician testing an industrial switchgear panel with a meter"></div>
  <div class="slider-pager"><span class="on">1</span><span>2</span><span>3</span><span>4</span></div>
  <svg class="slider-arrow" style="left:4px" width="30" height="46" viewBox="0 0 30 46"><path d="M26 2 L6 23 L26 44" fill="none" stroke="#fff" stroke-width="4"/></svg>
  <svg class="slider-arrow" style="right:4px" width="30" height="46" viewBox="0 0 30 46"><path d="M4 2 L24 23 L4 44" fill="none" stroke="#fff" stroke-width="4"/></svg>
  <div class="slider-caption cap-one">Electrical Installations</div>
  <div class="slider-caption cap-two">Commercial ✦ Industrial ✦ Domestic</div>
</section>

<nav class="main-nav abs">
  <ul><li>HOME</li><li>SERVICES</li><li>RESPONSABILITIES</li><li>CONTACT US</li></ul>
</nav>

<main class="intro abs">
  <h1>Welcome to Fenwold Electrical Services Limited</h1>
  <p>Established in 2005 Fenwold Electrical Services Limited is an independent company that has grown steadily over that period into a respected Commercial and Domestic Electrical installer providing it’s services nationwide.</p>
  <p>Professional and reliable, the secret of our success has come from recommendations from our customer base. Our staffing levels allow us to be flexible enough to tackle any size of project, contracts often exceeding 100K, yet we are able to complete the more modest budget competitively. All our work is guaranteed and our help line is always available to our clients to satisfy any after contract queries or concerns.</p>
  <p>As a company we strive to meet exceptional standards of workmanship, we are registered with the National Registry for Electrical Contractors and all our work is certificated accordingly. All our engineers are fully qualified in their relevant fields and all work there is carried out to BS 7671 standards.</p>
  <p>As Health and safety is always such a major factor in the industry, we always ensure that at least one qualified representative is present on each site. We also employ the services of health and safety consultants on a permanent basis.</p>
</main>

<section class="clients abs" aria-label="Clients">
  <div class="client"><i></i>Harlow Foods</div>
  <div class="client">Eastmarsh<br>Fire Service</div>
  <div class="client">Northcliff<br>District Council</div>
  <div class="client"><i></i>Garnet Seafood</div>
  <div class="client">Ashgrove Hotel</div>
</section>
<svg class="clients-tail abs" width="72" height="40" viewBox="0 0 72 40"><path d="M0 1 L12 38 L70 1" fill="#fff" stroke="#c8c8c8"/><path d="M1 0 H69" stroke="#fff" stroke-width="3"/></svg>
<div class="clients-label abs">Some of our client</div>

<aside class="sidebar abs">
  <h2>Our Services</h2>
  <div class="sidebar-photo" role="img" aria-label="Row of industrial switchgear cabinets"></div>
  <p class="sidebar-text">The Company is extensively experienced throughout a broad spectrum of electrical projects, which encompass:</p>
  <ul class="service-list"><li>Food Industry</li><li>Retail Premises</li><li>Councils</li><li>Schools and Colleges</li></ul>
  <div class="more">Learn more</div>
  <hr>
  <h2 class="social-title">Lets get social</h2>
  <div class="social"><span>Connect</span><span>Chirper</span><span>Circle</span></div>
</aside>

<footer class="footer abs">
  <h3 style="left:115px">Brows site</h3>
  <ul class="footer-links"><li>Home</li><li>Services</li><li>Responsabilities</li><li>Contact Us</li></ul>
  <div class="footer-rule" style="left:321px"></div>
  <h3 style="left:413px">What clinet say...</h3>
  <p class="quote">Lorem ipsum dolor sit amet, consectetuer adipiscing elit. Nam cursus. Morbi ut mi. Nullam enim leo, egestas id, condimentum at, laoreet mattis, massa. Sed eleifend nonummy diam. Nam cursus. Morbi ut mi. Nullam enim leo, egestas id.</p>
  <div class="quote-by">- R Holt</div>
  <div class="footer-rule" style="left:748px"></div>
  <h3 style="left:833px">Contact Info</h3>
  <div class="contact">
    <div>Unit 4b Harbour Park,<br>Kestrel Rd, DN40 2QX</div>
    <div class="tel"><b>Tel:</b>01632 960418</div>
  </div>
</footer>
<div class="base abs">Copyright © 2012 Fenwold Electrical Services Limited, All right reserves</div>

</body>
</html>
```